New, clean letterhead for law firm in Colorado using recently designed logo.

Professional letterhead for established law firm rebranding. We service high end clientele with mostly family law and personal injury cases. Need source files for future changes. Prefer logo at top, names of members and staff in left margin, contact info in footer.

Target Market(s)

High wealth individuals

Contact Information for Business Card

Need options for traditional and square two sided business cards

Font styles to use
Serif

Colors
0555a3

Requirements
Must have
• Our logo; blue, gray, and white; modern feel.
Should not have
• Images of people

```html
<!DOCTYPE html>
<html lang="en">
<head>
<meta charset="utf-8">
<title>Hartwell Lane Law, LLC – Letterhead</title>
<link href="https://fonts.googleapis.com/css2?family=Asap+Condensed:wght@400;600&family=Lato:wght@400&display=swap" rel="stylesheet">
<style>
  :root {
    --backdrop: #d6d6d6;
    --paper: #ffffff;
    --brand-blue: #1f68b0;
    --brand-gray: #9b9b9b;
    --body-text: #555555;
    --meta-text: #8c8c8c;
    --signature-tone: #dbe6f3;
  }
  * { box-sizing: border-box; margin: 0; padding: 0; }
  html, body {
    width: 1056px; height: 1200px; overflow: hidden;
    background: var(--backdrop);
  }
  .letterhead {
    position: absolute; left: 104px; top: 0;
    width: 848px; height: 1200px;
    background: var(--paper);
    overflow: hidden;
  }
  .firm-name {
    position: absolute; left: 79px; top: 122px; width: 260px;
    font-family: "Asap Condensed", sans-serif;
    font-weight: 600; font-size: 24px; letter-spacing: 1px;
    color: var(--brand-blue); text-transform: uppercase; line-height: 1.2;
  }
  .contact-block {
    position: absolute; left: 614px; top: 64px;
    font-family: "Lato", sans-serif; font-size: 14px; font-style: normal;
    color: var(--meta-text); line-height: 18px;
  }
  .contact-block .address { margin-bottom: 8px; }
  .contact-line { display: flex; align-items: center; height: 21px; }
  .contact-line svg { width: 13px; height: 13px; margin-right: 13px; flex: none; }
  .letter-body {
    position: absolute; left: 79px; top: 339px; width: 688px;
    font-family: "Asap Condensed", sans-serif; font-size: 20.8px;
    color: var(--body-text); line-height: 29.7px;
  }
  .letter-body p { text-align: justify; margin-bottom: 29px; }
  .letter-body .salutation { margin-bottom: 25px; }
  .closing {
    position: absolute; left: 79px; top: 941px;
    font-family: "Asap Condensed", sans-serif; font-size: 20.8px;
    color: var(--body-text); line-height: 30px;
  }
  .signature {
    position: absolute; left: 76px; top: 980px;
    width: 68px; height: 42px; background: var(--signature-tone); border-radius: 4px;
  }
  .footer-band {
    position: absolute; left: 228px; bottom: 0; width: 620px; height: 56px;
    background: linear-gradient(90deg, var(--brand-gray) 0%, var(--brand-blue) 45%, var(--brand-blue) 100%);
  }
</style>
</head>
<body>
<main class="letterhead">
  <header>
    <div class="firm-name">Hartwell Lane<br>Law, LLC</div>
    <address class="contact-block">
      <div class="address">1234 First Line Address<br>5678 Second Line Address</div>
      <div class="contact-line">
        <svg viewBox="0 0 16 16"><path fill="var(--brand-blue)" d="M3.5 1.5l2.3 2.6-1.3 1.7c.9 2 2.6 3.7 4.6 4.6l1.7-1.3 2.6 2.3-1.4 2.1C7.8 13.6 2.4 8.2 1.4 3z"/></svg>
        <span>1234567890</span>
      </div>
      <div class="contact-line">
        <svg viewBox="0 0 16 16"><rect x="1" y="3" width="14" height="10" fill="var(--brand-blue)"/><path d="M1.5 3.5L8 9l6.5-5.5M1.5 12.5l5-4.5M14.5 12.5l-5-4.5" stroke="#fff" stroke-width="1.2" fill="none"/></svg>
        <span>info@yourmail.com</span>
      </div>
      <div class="contact-line">
        <svg viewBox="0 0 16 16" fill="none" stroke="var(--brand-blue)" stroke-width="1.2"><circle cx="8" cy="8" r="6.5"/><ellipse cx="8" cy="8" rx="3" ry="6.5"/><path d="M1.5 8h13M2.5 4.8h11M2.5 11.2h11"/></svg>
        <span>www.yourwebsite.com</span>
      </div>
    </address>
  </header>

  <section class="letter-body">
    <p class="salutation">Dear Sir/Mam,</p>
    <p>Contrary to popular belief, Lorem Ipsum is not simply random text. It has roots in a piece of classical Latin literature from 45 BC, making it over 2000 years old. Daniel Ashcombe, a Latin professor at Alder Ridge College in Virginia, looked up one of the more obscure Latin words, consectetur.</p>
    <p>Lorem Ipsum comes from sections 1.10.32 and 1.10.33 of "de Finibus Bonorum et Malorum" (The Extremes of Good and Evil) by Aurelian Tace, written in 45 BC. This book is a treatise on the theory of ethics, very popular during the Renaissance. The first line of Lorem Ipsum.</p>
    <p>The standard chunk of Lorem Ipsum used since the 1500s is reproduced below for those interested. Sections 1.10.32 and 1.10.33 from "de Finibus Bonorum et Malorum" by Aurelian Tace are also reproduced in their exact original.</p>
    <p>The standard chunk of Lorem Ipsum used since the 1500s is reproduced below for those interested.</p>
  </section>

  <div class="closing">Best Regards</div>
  <div class="signature" role="img" aria-label="Handwritten signature of the sender"></div>

  <div class="footer-band" role="img" aria-label="Decorative gray and blue footer ornament"></div>
</main>
</body>
</html>
```